Brochure for handout and mailing

we market directly to small retail businesses. We provide personal attention to our clients to customize their applications to the lenders requirements. Small business owners do not have time to apply to the hundreds of lenders. We know which lenders are appropriate for your particular business. we make sure our clients are protected from unscrupulous lenders that lend money at rates that will damage a business. We really care about the ultimate success of our clients. we ant them to become a partner for years to come. One application will go to 5 hand picked lenders. We have a fast and secure online application. Funding in 7 days. Loan terms from 6 months to 5 years. Loan rates from 4% to 19%. Broker fees from 1% to 5%. We are a small family business ourselves with over 30 years experience. Integrity - Transparency. (we are not committed to the logo) (just designed it on Printolux.) would like to convert design to html or pdf version for email campaign also. Required Trifold Brochures (10.98" x 8.5"). I will be using printolux. They have a Brochure Template you can download.

Target Market(s)

Small Business Owners in the US

Industry/Entity Type

Retail

Font styles to use
Sans Serif

Colors
3176b5
85acd3
86cfc6

Requirements
Must have
• Full Bleed Size (starting document size)
• 11.10" x 8.63"
• 282 x 219 mm
• 3331 x 2588 pixels
• * Finished artwork should use the full bleed dimensions for best results.
• Document Trim Size (final size after being cut)
• 10.98" x 8.50"
• 279 x 216 mm
• 3295 x 2551 pixels
• * Please be sure to keep all text within the safe margin.
• Resolution
• 300 DPI
• * Dotted lines indicate where a fold will take place. If you don’t want copy or design to appear on the fold, make sure they stay within each panel’s safe margin. See full upload specifications at Printolux / brochures
Nice to have
• see www.quarrafundhub.com

```html
<!DOCTYPE html>
<html lang="en">
<head>
<meta charset="utf-8">
<title>QuarraFundHub Brochure</title>
<link href="https://fonts.googleapis.com/css2?family=Arimo:wght@400;500;600;700&display=swap" rel="stylesheet">
<style>
:root{
  --header-blue:#2f6fe3;
  --panel-grey:#edf1f1;
  --ink:#111;
  --green:#5ee08e;
  --green-bar:#6fe8a2;
  --red-bar:#e2431d;
  --orange:#eea020;
  --orange-bar:#f09a14;
  --white:#fff;
}
*{box-sizing:border-box;margin:0;padding:0}
html,body{width:1200px;height:932px;overflow:hidden;background:var(--white)}
body{position:relative;font-family:"Arimo",Arial,sans-serif;color:var(--ink)}
.photo{position:absolute}
.photo .inner{position:absolute;border:1px solid #fff;box-shadow:0 0 6px rgba(0,0,0,.35)}
.photo-owners{left:14px;top:14px;width:386px;height:316px;background:linear-gradient(90deg,#9a7a6a,#e9d9c8 50%,#a99a88)}
.photo-owners .inner{left:23px;top:20px;width:338px;height:278px;background:linear-gradient(160deg,#d6cfc6,#f1ece6 40%,#8ea77a 80%,#6e8d5a)}
.photo-florist{left:805px;top:14px;width:381px;height:316px;background:linear-gradient(90deg,#6a4a3a,#b7826a 50%,#2c3d55)}
.photo-florist .inner{left:18px;top:22px;width:345px;height:280px;background:linear-gradient(135deg,#a5543c,#d68aa5 40%,#3a4234 75%,#20302a)}
.bar-head{position:absolute;height:36px;background:var(--header-blue);color:var(--white);font-size:18px;font-weight:600;line-height:36px;padding-left:10px}
.panel{position:absolute;background:var(--panel-grey)}
.panel p,.step .text{font-size:12.4px;font-weight:500;line-height:27px;letter-spacing:.15px;hyphens:auto;-webkit-hyphens:auto}
.about{left:14px;top:388px;width:386px;height:544px;padding:13px 10px 0 10px;text-align:justify}
.about p+p{margin-top:24px}
.links{left:797px;top:403px;width:389px;height:529px;padding:7px 0 0 8px}
.links .item{margin-bottom:27px}
.links .url{padding-left:4px}
.links .url-long{padding-left:10px;padding-right:4px;word-break:break-all;hyphens:none}
.step{position:absolute;left:426px;width:344px}
.step .badge{position:absolute;left:0;top:0;width:88px;height:88px;border-radius:50%;display:flex;align-items:center;justify-content:center}
.step .label{position:absolute;left:74px;height:32px;width:268px;color:var(--white);font-size:17.5px;font-weight:600;line-height:32px;padding-left:18px}
.step .text{position:absolute;left:0;width:342px;text-align:justify}
.step-1 .badge{background:var(--green)}
.step-1 .label{background:var(--green-bar)}
.step-2 .badge{background:radial-gradient(circle at 50% 40%,#e04a22,#a82010)}
.step-2 .label{background:var(--red-bar)}
.step-3 .badge{background:var(--orange)}
.step-3 .label{background:var(--orange-bar)}
</style>
</head>
<body>

<div class="photo photo-owners" role="img" aria-label="Photo of a smiling couple of small shop owners standing in front of their store">
  <div class="inner"></div>
</div>

<div class="bar-head" style="left:407px;top:14px;width:386px;">How It Works</div>

<div class="photo photo-florist" role="img" aria-label="Photo of a florist in an apron standing in the doorway of her flower shop">
  <div class="inner"></div>
</div>

<section class="step step-1" style="top:76px;height:260px;">
  <div class="badge">
    <svg width="30" height="28" viewBox="0 0 30 28"><rect x="1" y="1" width="28" height="19" rx="1" fill="#fff"/><rect x="4" y="4" width="22" height="13" fill="#5ee08e"/><rect x="12" y="20" width="6" height="4" fill="#fff"/><rect x="8" y="24" width="14" height="2.5" fill="#fff"/></svg>
  </div>
  <div class="label" style="top:29px;">1. Secure Online Application</div>
  <p class="text" style="top:93px;">First create your own secure account. Before you can log in, an email will be sent to your email account in order to verify your identity. Then log in to your account and fill out the one page application. Come back to your account as often as you wish. Funding in 7 days.</p>
</section>

<section class="step step-2" style="top:369px;height:290px;">
  <div class="badge">
    <svg width="34" height="34" viewBox="0 0 34 34" fill="none" stroke="#fff" stroke-width="2.6" stroke-linecap="round"><circle cx="17" cy="19" r="11"/><path d="M17 12v7l4 3"/><path d="M4 8l5-5M30 8l-5-5"/><path d="M9 30l-2 3M25 30l2 3"/></svg>
  </div>
  <div class="label" style="top:32px;">2. We Select the Lender</div>
  <p class="text" style="top:94px;">We "curate" your application. We do a thorough analysis to make sure the package is complete. We carefully select the Lender that we know will be right for your business and you. One application goes to 5 hand picked lenders: terms from 6 months to 5 years, rates from 4% to 19%, broker fees from 1% to 5%.</p>
</section>

<section class="step step-3" style="top:666px;height:210px;">
  <div class="badge">
    <svg width="36" height="30" viewBox="0 0 36 30"><rect x="8" y="1" width="16" height="10" rx="1" fill="#fff" transform="rotate(-12 16 6)"/><rect x="2" y="8" width="30" height="20" rx="3" fill="#fff"/><rect x="24" y="14" width="10" height="8" rx="2" fill="#eea020"/><circle cx="28" cy="18" r="1.6" fill="#fff"/></svg>
  </div>
  <div class="label" style="top:28px;">3. We Review the Offer</div>
  <p class="text" style="top:93px;">As your personal advocate, we review the offer to make sure the lender understans your unique situation. If we agree that it is a great offer we will present it to you for your approval.</p>
</section>

<div class="bar-head" style="left:14px;top:352px;width:386px;">About Us</div>
<div class="panel about">
  <p>QuarraFundHub is the only company of its kind. We are a small, family business with over 30 years of experience and were founded on the principal that small business is the heart and soul of American capitalism, a necessary component of a free society. Small business must have easy access to many and varied financial resources in one place. While utilizing all the advantages of advanced technology, we strongly believe that only with personal attention can your business be successfully represented to lenders. We get to know you and your unique requirements. We match those requirements with the lenders requirements. We are a hybrid of state of the art technology and dedicated, personal attention.</p>
  <p>Many small business owners are simply too busy to find the right lender and many make the wrong choice - a choice which could have devastating consequences.</p>
  <p>CEO, Martin Alcott</p>
</div>

<div class="bar-head" style="left:797px;top:352px;width:389px;padding-left:18px;">Small Business Links</div>
<div class="panel links">
  <div class="item"><p>Telvora Small Business</p><p class="url">http://bizhub.telvora.com/</p><p>Interesting selected stories. Just might stimulate some new, creative thinking.</p></div>
  <div class="item"><p>Founders Weekly For Small Business</p><p class="url">http://www.foundersweekly.com/smbresourcecenter/#</p><p>More Ideas more stories.</p></div>
  <div class="item"><p>Federal Revenue Desk for Small Business</p><p class="url-long">http://www.revenuedesk.gov/Businesses/Small-Businesses-&amp;-Self-Employed/Small-Business-and-Self-Employed-Tax-Center-1</p><p>A must!</p></div>
  <div class="item"><p>Venture Journal</p><p class="url">http://www.venturejournal.com/</p><p>A standard for years. Some great articles.</p></div>
</div>

</body>
</html>
```